Cover needed for book, Wedded to the Fellow Who Drifted Out to Sea

Cover should use the attached photograph, with the groom faded in some way, to represent the concept in the title. Overall look should tell readers the book is in the genre of Marian's Embers, Never Send Us Back Home etc. Book is memoir of Edith, who was married to a man who had obsessive-compulsive disorder when little was known about the condition.

Text should be

Wedded to the Fellow Who Drifted Out to Sea
The true story of how obsession tore a family apart
By Edith Harcombe

```html
<!DOCTYPE html>
<html lang="en">
<head>
<meta charset="utf-8">
<title>Wedded to the Fellow Who Drifted Out to Sea — Cover</title>
<link rel="stylesheet" href="https://fonts.googleapis.com/css2?family=Cinzel:wght@400;500&family=EB+Garamond:wght@400&display=swap">
<style>
  :root {
    --backdrop: #c9d0cf;
    --cover: #000000;
    --ink: #ffffff;
    --glow: rgba(255, 255, 255, 0.55);
    --print-edge: #cdc5ba;
    --print-rim: #ece7df;
    --print-under: #bdbdba;
    --print-under-dark: #8e8e8b;
  }
  * { box-sizing: border-box; margin: 0; padding: 0; }
  html, body {
    width: 1200px;
    height: 800px;
    overflow: hidden;
    background: var(--backdrop);
  }
  .stage {
    width: 1200px;
    height: 800px;
    display: flex;
    align-items: center;
    justify-content: center;
  }
  .cover {
    position: relative;
    width: 538px;
    height: 800px;
    background: var(--cover);
    color: var(--ink);
    text-align: center;
    overflow: hidden;
  }
  .cover-title {
    position: absolute;
    top: 56px;
    left: 0;
    right: 0;
    font-family: "Cinzel", serif;
    font-weight: 400;
    line-height: 1;
  }
  .cover-title .title-main {
    display: block;
    font-size: 35px;
    letter-spacing: 1px;
  }
  .cover-title .title-sub {
    display: block;
    margin-top: 8px;
    font-size: 24px;
    letter-spacing: 1px;
  }
  .photo-stack {
    position: absolute;
    top: 134px;
    left: 52px;
    width: 436px;
    height: 556px;
  }
  .tagline {
    position: absolute;
    top: 690px;
    left: 0;
    right: 0;
    font-family: "EB Garamond", serif;
    font-size: 23px;
    text-shadow: 0 0 6px var(--glow);
  }
  .author {
    position: absolute;
    top: 728px;
    left: 0;
    right: 0;
    font-family: "Cinzel", serif;
    font-size: 36px;
    letter-spacing: 1px;
    text-shadow: 0 0 8px var(--glow);
  }
</style>
</head>
<body>
<main class="stage">
  <article class="cover">
    <h1 class="cover-title">
      <span class="title-main">Wedded to the Fellow</span>
      <span class="title-sub">Who Drifted Out to Sea</span>
    </h1>

    <svg class="photo-stack" viewBox="0 0 436 556">
      <defs>
        <linearGradient id="underPrint" x1="0" y1="0" x2="1" y2="1">
          <stop offset="0" stop-color="#cfcfcc"/>
          <stop offset="0.6" stop-color="var(--print-under)"/>
          <stop offset="1" stop-color="var(--print-under-dark)"/>
        </linearGradient>
        <linearGradient id="weddingPortrait" x1="0" y1="0.35" x2="1" y2="0.65">
          <stop offset="0" stop-color="#2e2e2d"/>
          <stop offset="0.3" stop-color="#4e4e4c"/>
          <stop offset="0.55" stop-color="#d8d8d4"/>
          <stop offset="0.8" stop-color="#b8b8b4"/>
          <stop offset="1" stop-color="#8a8a87"/>
        </linearGradient>
        <linearGradient id="portraitFloor" x1="0" y1="0" x2="0" y2="1">
          <stop offset="0.7" stop-color="#000" stop-opacity="0"/>
          <stop offset="1" stop-color="#1a1a1a" stop-opacity="0.75"/>
        </linearGradient>
        <clipPath id="tornPrint">
          <polygon points="54,320 70,300 66,290 88,270 100,262 112,236 128,220 140,196 158,178 170,150 190,136 208,118 224,110 238,92 262,80 282,62 300,52 318,38 337,24 413,24 428,519 61,529"/>
        </clipPath>
      </defs>

      <g class="print-stack-back">
        <rect x="4" y="26" width="396" height="520" rx="8" fill="#3e3e3c" transform="rotate(-1.5 200 290)"/>
        <rect x="12" y="16" width="398" height="520" rx="8" fill="#6c6c69" transform="rotate(-0.8 214 276)"/>
        <rect x="22" y="10" width="392" height="522" rx="6" fill="url(#underPrint)"/>
        <rect x="40" y="30" width="356" height="480" fill="none" stroke="#a9a9a6" stroke-width="2"/>
      </g>

      <polyline class="tear-rim" fill="none" stroke="var(--print-rim)" stroke-width="7" stroke-linejoin="round"
                points="50,322 66,300 62,290 84,270 96,262 108,236 124,220 136,196 154,178 166,150 186,136 204,118 220,110 234,92 258,80 278,62 296,52 314,38 335,20 413,20"/>

      <g class="print-front" clip-path="url(#tornPrint)">
        <rect x="40" y="16" width="392" height="520" fill="var(--print-edge)"/>
        <rect x="91" y="50" width="317" height="423" fill="url(#weddingPortrait)"
              role="img" aria-label="Black and white wedding portrait of a bride in a veil and long gown holding a bouquet, the groom beside her faded and torn away"/>
        <rect x="91" y="50" width="317" height="423" fill="url(#portraitFloor)"/>
      </g>
    </svg>

    <p class="tagline">The true story of how obsession tore a family apart by</p>
    <p class="author">Edith Harcombe</p>
  </article>
</main>
</body>
</html>
```